business cards for a home design center

Easy to read Business CArd I am uploading the logo. you will see the color scheme we need.
Also after the design of the business card I need to be changing the employee name and cel phone. as needed.
I want to try those clear business cards and also not clear ones.
I want for business card to be transitional not too busy, and not that plain. hopw you can get my feeling.
I think the logo I attached will help you understand more the consept

Target Market(s)

Builders in town, people building home, office, commercial residential.

Industry/Entity Type

Home Improvement

Contact Information for Business Card

Marisol Quintero
Office-958-341-2265
Fax 958-341-2290
Cell 958-5204316
website. www.velmontinteriorhall.com
email marisol@velmontinteriorhall.com

Requirements
Must have
• Elegant, sleek,
Nice to have
• write on the back of the card like appointments or notes
Should not have
• Not all black

```html
<!DOCTYPE html>
<html lang="en">
<head>
<meta charset="utf-8">
<title>Velmont Interior Hall — Business Card</title>
<link rel="stylesheet" href="https://fonts.googleapis.com/css2?family=Open+Sans:wght@400;600;700&display=swap">
<style>
  :root {
    --page: #ecebe8;
    --card: #ffffff;
    --gold: #efb01c;
    --charcoal: #333236;
    --ink: #1f1f22;
    --light-text: #ffffff;
  }
  * { box-sizing: border-box; margin: 0; padding: 0; }
  html, body {
    width: 1200px; height: 1023px; overflow: hidden;
    background: var(--page);
    font-family: "Open Sans", Arial, sans-serif;
  }
  .sheet {
    width: 1200px; height: 1023px;
    display: flex; flex-direction: column; align-items: center; justify-content: center;
    gap: 30px;
  }
  .card {
    position: relative;
    width: 840px; height: 480px;
    background: var(--card);
    overflow: hidden;
    box-shadow: 0 6px 22px rgba(0,0,0,.14);
  }
  .top-accent {
    position: absolute; top: 0; left: 120px;
    width: 190px; height: 14px; background: var(--gold);
  }
  .brand {
    position: absolute; left: 70px; top: 150px;
    display: flex; align-items: center; gap: 16px;
  }
  .brand-mark {
    width: 46px; height: 46px; border-radius: 50%; background: var(--gold);
  }
  .brand-name {
    font-weight: 700; font-size: 40px; color: var(--ink); line-height: 1.05;
  }
  .person {
    position: absolute; right: 60px; top: 70px; text-align: right; color: var(--ink);
  }
  .person-name { font-weight: 700; font-size: 22px; letter-spacing: .5px; text-transform: uppercase; }
  .person-title { font-weight: 400; font-size: 19px; text-transform: uppercase; margin-top: 2px; }
  .bands { position: absolute; inset: 0; }
  .address {
    position: absolute; right: 50px; top: 200px;
    color: var(--light-text); font-size: 18px; line-height: 1.35;
    display: flex; gap: 10px; align-items: flex-start;
  }
  .address svg { margin-top: 3px; flex: none; }
  .contacts {
    position: absolute; left: 380px; top: 322px;
    list-style: none; color: var(--light-text);
    font-size: 19px; line-height: 1.5;
  }
  .contacts li { display: flex; align-items: center; gap: 12px; }
  .icon {
    width: 18px; height: 18px; background: var(--gold); border-radius: 2px;
    display: flex; align-items: center; justify-content: center; flex: none;
  }
  .card-back .bottom-accent {
    position: absolute; bottom: 0; left: 330px;
    width: 200px; height: 16px; background: var(--gold);
  }
</style>
</head>
<body>
<main class="sheet">

  <section class="card card-front" aria-label="Business card front">
    <svg class="bands" width="840" height="480" viewBox="0 0 840 480" aria-hidden="true">
      <polygon points="560,175 840,175 840,300 380,300" fill="var(--gold)"/>
      <polygon points="380,300 840,300 840,480 340,480 340,300" fill="var(--charcoal)"/>
      <rect x="340" y="300" width="60" height="180" fill="var(--charcoal)"/>
    </svg>

    <div class="top-accent"></div>

    <div class="brand">
      <span class="brand-mark"></span>
      <span class="brand-name">Velmont<br>Interior Hall</span>
    </div>

    <div class="person">
      <p class="person-name">Marisol Quintero</p>
      <p class="person-title">Director</p>
    </div>

    <div class="address">
      <svg width="16" height="20" viewBox="0 0 16 20" aria-hidden="true">
        <rect width="16" height="20" rx="2" fill="#fff"/>
        <path d="M8 3a4 4 0 0 0-4 4c0 3 4 8 4 8s4-5 4-8a4 4 0 0 0-4-4zm0 5.5A1.5 1.5 0 1 1 8 5.5a1.5 1.5 0 0 1 0 3z" fill="var(--gold)"/>
      </svg>
      <p>17 Larkfield Avenue<br>Tampa FL 3361</p>
    </div>

    <ul class="contacts">
      <li><span class="icon"><svg width="12" height="12" viewBox="0 0 12 12"><rect x="3.5" y="1" width="5" height="10" rx="1" fill="var(--charcoal)"/></svg></span>958-5204316</li>
      <li><span class="icon"><svg width="12" height="12" viewBox="0 0 12 12"><path d="M2 2l2-1 1.5 3-1 1a6 6 0 0 0 2.5 2.5l1-1 3 1.5-1 2C5 10 2 7 2 2z" fill="var(--charcoal)"/></svg></span>958-341-2265</li>
      <li><span class="icon"><svg width="12" height="12" viewBox="0 0 12 12"><rect x="1.5" y="4" width="9" height="6" fill="var(--charcoal)"/><rect x="3.5" y="1.5" width="5" height="3" fill="var(--charcoal)"/></svg></span>958-341-2290</li>
      <li><span class="icon"><svg width="12" height="12" viewBox="0 0 12 12"><circle cx="6" cy="6" r="4.5" fill="none" stroke="var(--charcoal)" stroke-width="1.4"/><path d="M1.5 6h9M6 1.5c-2 2.5-2 6.5 0 9M6 1.5c2 2.5 2 6.5 0 9" fill="none" stroke="var(--charcoal)" stroke-width="1"/></svg></span>www.velmontinteriorhall.com</li>
      <li><span class="icon"><svg width="12" height="12" viewBox="0 0 12 12"><rect x="1.5" y="3" width="9" height="6.5" fill="var(--charcoal)"/><path d="M1.5 3l4.5 3.5L10.5 3" fill="none" stroke="var(--gold)" stroke-width="1"/></svg></span>marisol@velmontinteriorhall.com</li>
    </ul>
  </section>

  <section class="card card-back" aria-label="Business card back">
    <div class="bottom-accent"></div>
  </section>

</main>
</body>
</html>
```